Promotional brochure for educational consulting firm

Hi Designers!

Please do a 8.5 x 11 inch tri-fold brochure as well as a 8.5 x 11 inch half-fold brochure.  I appreciate black and white versions in addition to color.  Please take a look at my company's website for a better sense of the look and feel I am going for:  www.brightlarkedu.org

Thanks!

Industry/Entity Type

Consulting

Colors
3176b5
85abd2
fcfbfd

```html
<!DOCTYPE html>
<html lang="en">
<head>
<meta charset="utf-8">
<title>Brightlark Associates – Tri-fold Brochure Outside</title>
<link rel="stylesheet" href="https://fonts.googleapis.com/css2?family=Jost:wght@400;500;700&display=swap">
<style>
  :root {
    --brand-blue: #3176b5;
    --brand-sky: #85abd2;
    --paper: #fcfbfd;
    --stage: #5a5a5a;
    --fold-line: #d9dde3;
    --ink-gray: #8c8c8c;
    --photo-a-1: #c9d6e4;
    --photo-a-2: #3a3d55;
    --photo-b-1: #e6c9a8;
    --photo-b-2: #2b2b33;
  }
  * { box-sizing: border-box; margin: 0; padding: 0; }
  html, body {
    width: 1200px; height: 841px; overflow: hidden;
    background: var(--stage);
    font-family: "Jost", "Futura", sans-serif;
  }
  .brochure {
    position: absolute; left: 80px; top: 18px;
    width: 1040px; height: 804px;
    background: var(--paper);
    display: flex;
    box-shadow: 0 6px 24px rgba(0,0,0,.35);
  }
  .panel {
    position: relative; width: 346.67px; height: 100%;
    border-right: 1px solid var(--fold-line);
  }
  .panel:last-child { border-right: none; }

  /* Left panel */
  .photo-frame {
    position: absolute; left: 18px;
    width: 300px; height: 230px;
    border: 2px solid var(--brand-blue);
    padding: 10px;
  }
  .photo-frame--top { top: 14px; border-top: none; border-left: none; border-radius: 0 0 22px 0; }
  .photo-frame--bottom { bottom: 14px; border-bottom: none; border-left: none; border-radius: 0 22px 0 0; }
  .photo { width: 100%; height: 100%; border-radius: 14px; }
  .photo--globe { background: linear-gradient(135deg, var(--photo-a-1), #f3f5f8 45%, var(--photo-a-2)); }
  .photo--reading { background: linear-gradient(120deg, #f4efe6, var(--photo-b-1) 45%, var(--photo-b-2)); }

  .tagline-box {
    position: absolute; left: 42px; top: 318px;
    width: 262px; padding: 14px 18px 16px;
    border: 2px solid var(--brand-blue); border-radius: 22px;
    text-align: center;
  }
  .tagline-lead { color: var(--brand-blue); font-size: 24px; line-height: 1.1; }
  .tagline-figure { color: var(--ink-gray); font-size: 42px; font-weight: 700; letter-spacing: 1px; line-height: 1.1; }

  /* Middle panel */
  .contact-heading {
    position: absolute; top: 150px; width: 100%;
    text-align: center; color: var(--brand-blue);
    font-size: 38px; font-weight: 400;
  }
  .contact-box {
    position: absolute; left: 42px; top: 218px; width: 262px;
    padding: 18px 14px 20px;
    border: 2px solid var(--brand-blue); border-radius: 26px;
    color: var(--brand-blue); font-size: 19px; line-height: 1.35;
    text-align: center; list-style: none;
  }
  .contact-label { display: inline-block; width: 24px; }

  .wordmark {
    position: absolute; width: 100%; text-align: center;
  }
  .wordmark--middle { top: 540px; }
  .wordmark--cover { top: 230px; }
  .wordmark-dot {
    display: block; width: 44px; height: 44px; margin: 0 auto 10px;
    border-radius: 50%; background: var(--brand-blue);
  }
  .wordmark-name {
    color: var(--brand-blue); font-size: 17px; font-weight: 500;
    letter-spacing: 1px; text-transform: uppercase;
  }
  .wordmark-sub {
    color: var(--brand-sky); font-size: 10.5px; letter-spacing: .6px;
    text-transform: uppercase; margin-top: 2px;
  }
</style>
</head>
<body>
  <main class="brochure">
    <section class="panel panel--inside-flap">
      <div class="photo-frame photo-frame--top">
        <div class="photo photo--globe" role="img" aria-label="Photo of two young students in uniform examining a globe with a magnifying glass"></div>
      </div>
      <div class="tagline-box">
        <p class="tagline-lead">School leadership is</p>
        <p class="tagline-figure">24/7/365</p>
      </div>
      <div class="photo-frame photo-frame--bottom">
        <div class="photo photo--reading" role="img" aria-label="Photo of a student reading printed pages at a classroom table"></div>
      </div>
    </section>

    <section class="panel panel--back">
      <h2 class="contact-heading">Contact Us</h2>
      <ul class="contact-box">
        <li>Dana Whitfield, Ed.D.</li>
        <li><span class="contact-label">[t]</span> 626.555.0142</li>
        <li><span class="contact-label">[f]</span> 626.555.0187</li>
        <li>dana@brightlarkedu.org</li>
        <li>www.brightlarkedu.org</li>
      </ul>
      <div class="wordmark wordmark--middle">
        <span class="wordmark-dot"></span>
        <p class="wordmark-name">Brightlark Associates LLC</p>
        <p class="wordmark-sub">Supporting schools &amp; school leaders</p>
      </div>
    </section>

    <section class="panel panel--cover">
      <div class="wordmark wordmark--cover">
        <span class="wordmark-dot"></span>
        <p class="wordmark-name">Brightlark Associates LLC</p>
        <p class="wordmark-sub">Supporting schools &amp; school leaders</p>
      </div>
    </section>
  </main>
</body>
</html>
```